Modern, colorful Webdesign for SunnyPawTots: kids yoga, kids music and kids books

We need a new website design! www.sunnypawtots.de
- I started working on my website by buying a theme. But I don´t like it. And I can not adjust it to my needs. I need a new Design that transports the style and feeling of my logo and my concept
- Sunny Paw Tots sells services and products in the 3 main areas: 1. Kids Yoga, 2. Kids Stories/Books, 3. Kids Music, Crafting is included in some of the products
- Our Concept: Our products stand out from other products in their fields by bringing these different areas together and unite them to provide even more positive effects on the child´s development. For example: A Book is not only a book! It comes with a song and crafting elements inside the book. A Live Yoga session is not only movement and meditation, it incorporates also music, dancing and crafting. A live music class also incorporates international songs and yoga elements.
- Markets: Germany and USA/UK
- Target groups: mothers, fathers, caregivers, families with kids (age 0-10), well educated with middle to high income
- Business target groups: preschools, elementary schools, small businesses (for events), kids TV and radio programs, book stores, crafting stores
- Look & feel of the website: modern, playful, colorful

caregivers, moms, dads, grandparents, day cares, schools,

kids yoga, kids music, kids books, crafting

5+ page

Sans Serif

• video/picture slider, colorful icons, overview of all icons, grafic to explain the concept
• Bring icons with products together. Show an interesting way to explain the concept of the brand with the icons and the bear.

```html
<!DOCTYPE html>
<html lang="en">
<head>
<meta charset="utf-8">
<title>SunnyPawTots – Kids Yoga, Stories, Music</title>
<link rel="stylesheet" href="https://fonts.googleapis.com/css2?family=Roboto:wght@400;500;700;900&display=swap">
<style>
:root{
  --blue:#2b4ee8;
  --magenta:#c2259f;
  --purple:#8a2bd1;
  --orange:#ee8a2e;
  --ink:#222;
  --muted:#6d6d6d;
  --paper:#ffffff;
  --soft:#f4f4f4;
  --footer:#1e1e1e;
  --brand-grad:linear-gradient(90deg,var(--blue) 0%,var(--magenta) 55%,var(--orange) 100%);
  --btn-grad:linear-gradient(90deg,#c0229e 0%,#ee8a2e 100%);
}
*{box-sizing:border-box;margin:0;padding:0}
html,body{width:1200px;height:3590px;overflow:hidden}
body{position:relative;font-family:"Roboto",Arial,sans-serif;color:var(--ink);background:var(--paper)}
.abs{position:absolute}
.grad-text{display:inline-block;background:var(--brand-grad);-webkit-background-clip:text;background-clip:text;color:transparent}
.btn{position:absolute;display:flex;align-items:center;justify-content:center;border-radius:30px;background:var(--btn-grad);color:#fff;font-weight:700;font-size:14px;letter-spacing:.2px}

/* header */
.topline{left:0;top:0;width:1200px;height:4px;background:var(--orange);z-index:5}
.header{left:0;top:0;width:1200px;height:94px;background:#fff;z-index:3}
.logo-badge{left:76px;top:-28px;width:188px;height:188px;border-radius:50%;background:#fff;z-index:4;display:flex;align-items:center;justify-content:center;padding-top:60px}
.brand-name{font-weight:900;font-size:21px;color:var(--magenta)}
.nav{top:43px;font-size:12px;font-weight:500;color:var(--ink);z-index:4;letter-spacing:.2px}
.call-icon{left:885px;top:28px;width:44px;height:44px;border-radius:50%;background:var(--btn-grad);z-index:4;display:flex;align-items:center;justify-content:center}
.call-label{left:948px;top:32px;font-size:12px;color:var(--muted);z-index:4}
.call-num{left:948px;top:52px;font-size:14px;font-weight:500;z-index:4}

/* hero */
.hero-photo{left:0;top:94px;width:1200px;height:650px;background:
  radial-gradient(ellipse 150px 190px at 270px 330px,rgba(214,40,110,.85),rgba(214,40,110,0) 100%),
  radial-gradient(ellipse 110px 90px at 280px 210px,rgba(238,196,160,.9),rgba(238,196,160,0) 100%),
  radial-gradient(ellipse 260px 90px at 300px 530px,rgba(40,38,52,.75),rgba(40,38,52,0) 100%),
  radial-gradient(ellipse 500px 120px at 330px 600px,rgba(230,80,140,.75),rgba(230,80,140,0) 100%),
  radial-gradient(ellipse 300px 140px at 250px 140px,rgba(255,255,255,.9),rgba(255,255,255,0) 100%),
  radial-gradient(ellipse 80px 110px at 980px 90px,rgba(200,175,150,.7),rgba(200,175,150,0) 100%),
  linear-gradient(180deg,#f1ece7 0%,#ebe4de 55%,#d9cdc6 75%,#cfc1b9 100%)}
.hero-card{left:599px;top:247px;width:489px;height:244px;border-radius:14px;background:rgba(255,255,255,.9)}
.hero-title{left:627px;top:268px;font-size:38px;font-weight:900}
.hero-text{left:627px;top:329px;width:440px;font-size:16px;line-height:29px;font-weight:500;color:#333}
.slider-arrow{top:368px;z-index:2}

/* welcome */
.welcome-title{left:111px;top:800px;font-size:34px;font-weight:900;line-height:44px}
.welcome-text{left:111px;width:492px;font-size:13px;line-height:25.7px;color:var(--muted)}
.welcome-photo{left:676px;top:795px;width:412px;height:412px;border-radius:50%;background:
  radial-gradient(ellipse 80px 150px at 330px 260px,rgba(30,32,44,.95),rgba(30,32,44,0) 100%),
  radial-gradient(ellipse 90px 130px at 130px 260px,rgba(120,110,100,.85),rgba(120,110,100,0) 100%),
  radial-gradient(ellipse 70px 90px at 180px 140px,rgba(220,170,160,.85),rgba(220,170,160,0) 100%),
  radial-gradient(ellipse 140px 50px at 220px 270px,rgba(180,150,120,.7),rgba(180,150,120,0) 100%),
  linear-gradient(160deg,#eef0f1 0%,#d8dad9 45%,#8a8480 80%,#4a4a55 100%)}

/* featured */
.featured{left:0;top:1296px;width:1200px;height:616px;background:var(--soft)}
.title-row{left:0;width:1200px;text-align:center}
.section-title{font-size:34px;font-weight:900}
.video-frame{left:258px;top:1451px;width:686px;height:386px;background:#fff;border-radius:6px;box-shadow:0 2px 10px rgba(0,0,0,.12)}
.video-still{left:266px;top:1459px;width:669px;height:370px;background:
  radial-gradient(ellipse 90px 150px at 430px 130px,rgba(70,45,40,.6),rgba(70,45,40,0) 100%),
  radial-gradient(ellipse 110px 140px at 320px 250px,rgba(210,200,190,.9),rgba(210,200,190,0) 100%),
  radial-gradient(ellipse 120px 130px at 440px 250px,rgba(225,220,212,.95),rgba(225,220,212,0) 100%),
  radial-gradient(ellipse 160px 50px at 370px 345px,rgba(90,85,95,.7),rgba(90,85,95,0) 100%),
  radial-gradient(ellipse 60px 80px at 610px 110px,rgba(150,110,80,.6),rgba(150,110,80,0) 100%),
  linear-gradient(120deg,#f2efeb 0%,#e2dcd5 50%,#c8bcb2 100%)}
.play{left:563px;top:1606px}
.side-thumb{top:1546px;width:174px;height:196px}

/* categories */
.categories{left:0;top:1912px;width:1200px;height:612px;background:
  radial-gradient(ellipse 220px 180px at 830px 330px,rgba(255,220,180,.25),rgba(255,220,180,0) 100%),
  radial-gradient(ellipse 260px 160px at 200px 450px,rgba(255,255,255,.12),rgba(255,255,255,0) 100%),
  linear-gradient(100deg,#c0229e 0%,#d6498a 45%,#ea8a4e 100%)}
.cat-title{top:1957px;color:#fff}
.cat-head{font-size:20px;font-weight:700;color:#fff}
.cat-item{font-size:14px;color:#fff;display:flex;align-items:center;gap:18px}
.cat-item svg{flex:none}
.core{left:188px;top:2102px;width:304px;height:304px;border-radius:50%;background:#fff;display:flex;align-items:center;justify-content:center}
.icon-dot{width:78px;height:78px;border-radius:50%;background:#fff;display:flex;align-items:center;justify-content:center}

/* gallery */
.gallery-tile{width:313px;height:213px;border-radius:4px}

/* footer */
.footer{left:0;top:3233px;width:1200px;height:357px;background:var(--footer)}
.foot-nav{left:0;top:3384px;width:1200px;display:flex;justify-content:center;gap:22px;color:#fff;font-size:16px;font-weight:700}
.foot-contact{left:0;top:3426px;width:1200px;display:flex;justify-content:center;align-items:center;gap:14px;color:#fff;font-size:16px;font-weight:500}
.social{top:3469px;width:34px;height:34px;border-radius:50%;background:#fff;box-shadow:inset 0 0 0 9px #fff,inset 0 0 0 40px #e9e9e9}
.social.first{background:var(--btn-grad);box-shadow:none}
.foot-rule{left:111px;top:3530px;width:977px;height:1px;background:#3a3a3a}
.copyright{left:0;top:3551px;width:1200px;text-align:center;color:#fff;font-size:12px}
</style>
</head>
<body>

<div class="abs topline"></div>
<header class="abs header"></header>
<div class="abs logo-badge"><span class="brand-name">SunnyPawTots</span></div>
<nav>
  <span class="abs nav" style="left:301px">YOGA</span>
  <span class="abs nav" style="left:357px">STORIES</span>
  <span class="abs nav" style="left:431px">MUSIC</span>
  <span class="abs nav" style="left:493px">SECRET SONG</span>
  <span class="abs nav" style="left:600px">CRAFTING</span>
  <span class="abs nav" style="left:684px">OUR CONCEPT</span>
  <span class="abs nav" style="left:794px">CONTACT</span>
</nav>
<div class="abs call-icon">
  <svg width="18" height="18" viewBox="0 0 24 24"><path fill="#fff" d="M6.6 10.8a15.1 15.1 0 0 0 6.6 6.6l2.2-2.2a1 1 0 0 1 1-.25 11.4 11.4 0 0 0 3.6.57 1 1 0 0 1 1 1V20a1 1 0 0 1-1 1A17 17 0 0 1 3 4a1 1 0 0 1 1-1h3.5a1 1 0 0 1 1 1c0 1.25.2 2.45.57 3.57a1 1 0 0 1-.25 1z"/></svg>
</div>
<span class="abs call-label">CALL US:</span>
<span class="abs call-num">+61 (0) 3 9000 1234</span>

<!-- hero slider -->
<div class="abs hero-photo" role="img" aria-label="Photo of a young girl meditating cross-legged on a pink yoga mat in a bright living room"></div>
<div class="abs hero-card"></div>
<h1 class="abs hero-title grad-text">YOGA FOR CHILDREN</h1>
<p class="abs hero-text">But they also subsidized both the terminal and the just two pains. Let the clita kasd gubergren</p>
<span class="btn" style="left:627px;top:408px;width:154px;height:49px">GET STARTED</span>
<svg class="abs slider-arrow" style="left:36px" width="24" height="34" viewBox="0 0 24 34"><path d="M18 3 5 17l13 14" fill="none" stroke="#fff" stroke-width="3.5" stroke-linecap="round"/></svg>
<svg class="abs slider-arrow" style="left:1140px" width="24" height="34" viewBox="0 0 24 34"><path d="M6 3l13 14L6 31" fill="none" stroke="#fff" stroke-width="3.5" stroke-linecap="round"/></svg>

<svg class="abs" style="left:0;top:590px" width="1200" height="170" viewBox="0 0 1200 170">
  <defs>
    <linearGradient id="wave" x1="0" x2="1" y1="0" y2="0">
      <stop offset="0" stop-color="#9a2bd0"/><stop offset=".45" stop-color="#8a2bd1"/><stop offset="1" stop-color="#c0229e"/>
    </linearGradient>
  </defs>
  <path d="M0 44C80 110 180 150 280 146 420 140 520 85 620 50 760 10 960 10 1200 120V170H0Z" fill="#fff"/>
  <path d="M0 44C80 110 180 150 280 146 420 140 520 85 620 50 760 10 960 10 1200 120" fill="none" stroke="url(#wave)" stroke-width="9"/>
  <circle cx="600" cy="79" r="62" fill="none" stroke="#fff" stroke-width="2"/>
  <circle cx="600" cy="79" r="48" fill="#fff"/>
  <circle cx="600" cy="79" r="16" fill="none" stroke="#c0229e" stroke-width="3"/>
</svg>

<!-- welcome -->
<h2 class="abs welcome-title grad-text">WELCOME TO SUNNY<br>PAW TOTS</h2>
<p class="abs welcome-text" style="top:911px">The pain itself is a lot of pain, it has been sadipscing over the years, but it is time to envy the pain and the pain is exciting, it was exciting, it was complicated. But they also subsidized both the terminal and the just two pains. Let the clita kasd gubergren, no sea takimata be holy</p>
<p class="abs welcome-text" style="top:1025px">The pain itself is a lot of pain, it has been sadipscing over the years, but it is time to envy the pain and the pain is exciting, it was exciting, it was complicated. But they also subsidized both the terminal and the just two pains.</p>
<span class="btn" style="left:111px;top:1143px;width:154px;height:51px">GET STARTED</span>
<div class="abs welcome-photo" role="img" aria-label="Photo of parents talking with an advisor at a table"></div>

<!-- featured videos -->
<section class="abs featured"></section>
<div class="abs title-row" style="top:1362px"><h2 class="section-title grad-text">FEATURED VIDEOS</h2></div>
<div class="abs side-thumb" style="left:0;background:radial-gradient(ellipse 60px 70px at 60px 70px,rgba(235,195,165,.9),rgba(235,195,165,0) 100%),radial-gradient(ellipse 70px 60px at 110px 140px,rgba(110,70,50,.85),rgba(110,70,50,0) 100%),linear-gradient(120deg,#2f3340,#6a6f80 45%,#c9b7a5)" role="img" aria-label="Photo of a girl playing the violin"></div>
<div class="abs side-thumb" style="left:1027px;background:radial-gradient(ellipse 60px 60px at 70px 70px,rgba(240,150,170,.9),rgba(240,150,170,0) 100%),radial-gradient(ellipse 90px 40px at 110px 170px,rgba(250,220,60,.9),rgba(250,220,60,0) 100%),linear-gradient(120deg,#f3dcd6,#e9c7a8 50%,#9fd2e5)" role="img" aria-label="Photo of children crafting at a table"></div>
<svg class="abs" style="left:203px;top:1631px" width="26" height="26" viewBox="0 0 26 26"><path d="M18 3 7 13l11 10" fill="none" stroke="#c0229e" stroke-width="5"/><path d="M18 3 7 13l11 10" fill="none" stroke="#333" stroke-width="2"/></svg>
<svg class="abs" style="left:971px;top:1631px" width="26" height="26" viewBox="0 0 26 26"><path d="M8 3l11 10L8 23" fill="none" stroke="#c0229e" stroke-width="5"/><path d="M8 3l11 10L8 23" fill="none" stroke="#333" stroke-width="2"/></svg>
<div class="abs video-frame"></div>
<div class="abs video-still" role="img" aria-label="Video still of a mother and daughter meditating together"></div>
<svg class="abs play" width="76" height="76" viewBox="0 0 76 76"><circle cx="38" cy="38" r="34" fill="none" stroke="#fff" stroke-width="3"/><circle cx="38" cy="38" r="22" fill="#fff"/><path d="M33 29l12 9-12 9z" fill="#c0229e"/></svg>

<!-- categories -->
<section class="abs categories" role="img" aria-label="Faded photo of kids doing yoga under a magenta to orange gradient"></section>
<div class="abs title-row cat-title"><h2 class="section-title">OUR CATEGORIES</h2></div>
<svg class="abs" style="left:0;top:1912px" width="1200" height="612" viewBox="0 1912 1200 612">
  <circle cx="340" cy="2254" r="171" fill="none" stroke="#fff" stroke-width="2"/>
  <polyline points="453,2125 502,2079 644,2079" fill="none" stroke="#fff" stroke-width="2"/>
  <line x1="512" y1="2254" x2="644" y2="2254" stroke="#fff" stroke-width="2"/>
  <polyline points="453,2383 502,2431 644,2431" fill="none" stroke="#fff" stroke-width="2"/>
  <circle cx="453" cy="2125" r="6" fill="#fff" stroke="#e07a7a" stroke-width="2"/>
  <circle cx="512" cy="2254" r="6" fill="#fff" stroke="#e07a7a" stroke-width="2"/>
  <circle cx="453" cy="2383" r="6" fill="#fff" stroke="#e07a7a" stroke-width="2"/>
  <circle cx="644" cy="2254" r="48" fill="none" stroke="#fff" stroke-width="3"/>
</svg>
<div class="abs core"><span class="brand-name" style="font-size:26px">SunnyPawTots</span></div>

<div class="abs icon-dot" style="left:605px;top:2040px">
  <svg width="38" height="38" viewBox="0 0 38 38" fill="none" stroke="#c0229e" stroke-width="2.2" stroke-linecap="round"><circle cx="19" cy="7" r="4"/><path d="M7 14h24M19 14v10l-7 9M19 24l7 9"/></svg>
</div>
<div class="abs icon-dot" style="left:605px;top:2215px;background:var(--btn-grad)">
  <svg width="38" height="38" viewBox="0 0 38 38" fill="none" stroke="#fff" stroke-width="2.2" stroke-linejoin="round"><path d="M4 10c5-2 10-2 15 2 5-4 10-4 15-2v20c-5-2-10-2-15 2-5-4-10-4-15-2z"/><path d="M19 12v20"/></svg>
</div>
<div class="abs icon-dot" style="left:605px;top:2392px">
  <svg width="38" height="38" viewBox="0 0 38 38" fill="none" stroke="#c0229e" stroke-width="2.2" stroke-linecap="round"><path d="M5 9h22M5 16h22M5 23h14M5 30h14M27 16v14"/><circle cx="24" cy="30" r="3"/></svg>
</div>

<svg width="0" height="0" style="position:absolute"><defs><symbol id="bullet" viewBox="0 0 14 14"><circle cx="7" cy="7" r="7" fill="#fff"/><path d="M4 7h6M7.5 4.5 10 7l-2.5 2.5" fill="none" stroke="#d6498a" stroke-width="1.6" stroke-linecap="round"/></symbol></defs></svg>

<div class="abs cat-head" style="left:736px;top:2036px">YOGA</div>
<div class="abs cat-item" style="left:736px;top:2079px"><svg width="14" height="14"><use href="#bullet"/></svg>Yoga video course</div>
<div class="abs cat-item" style="left:736px;top:2107px"><svg width="14" height="14"><use href="#bullet"/></svg>Yoga live</div>
<div class="abs cat-item" style="left:736px;top:2135px"><svg width="14" height="14"><use href="#bullet"/></svg>Yoga event</div>
<div class="abs cat-head" style="left:736px;top:2195px">STORIES</div>
<div class="abs cat-item" style="left:736px;top:2238px"><svg width="14" height="14"><use href="#bullet"/></svg>Unicorn Mila in the manger Book</div>
<div class="abs cat-item" style="left:736px;top:2266px"><svg width="14" height="14"><use href="#bullet"/></svg>Dinosaur Timo in the manger Book</div>
<div class="abs cat-item" style="left:736px;top:2293px"><svg width="14" height="14"><use href="#bullet"/></svg>Yoga video course</div>
<div class="abs cat-head" style="left:736px;top:2356px">MUSIC</div>
<div class="abs cat-item" style="left:736px;top:2399px"><svg width="14" height="14"><use href="#bullet"/></svg>Songs</div>
<div class="abs cat-item" style="left:736px;top:2427px"><svg width="14" height="14"><use href="#bullet"/></svg>Live classes international music program</div>
<div class="abs cat-item" style="left:736px;top:2455px"><svg width="14" height="14"><use href="#bullet"/></svg>Music events</div>

<!-- gallery -->
<div class="abs title-row" style="top:2612px"><h2 class="section-title grad-text">OUR GALLERY</h2></div>
<div class="abs gallery-tile" style="left:111px;top:2693px;background:radial-gradient(ellipse 70px 90px at 60px 130px,rgba(90,60,45,.85),rgba(90,60,45,0) 100%),radial-gradient(ellipse 80px 30px at 190px 180px,rgba(20,20,24,.8),rgba(20,20,24,0) 100%),radial-gradient(ellipse 60px 90px at 280px 110px,rgba(160,60,70,.7),rgba(160,60,70,0) 100%),linear-gradient(120deg,#3b2f2a,#9a7f70 50%,#d9cbbf)" role="img" aria-label="Photo of a piano lesson for children"></div>
<div class="abs gallery-tile" style="left:443px;top:2693px;background:radial-gradient(ellipse 70px 60px at 80px 130px,rgba(250,215,60,.9),rgba(250,215,60,0) 100%),radial-gradient(ellipse 60px 70px at 170px 80px,rgba(240,150,175,.9),rgba(240,150,175,0) 100%),radial-gradient(ellipse 80px 50px at 170px 190px,rgba(110,190,80,.7),rgba(110,190,80,0) 100%),linear-gradient(120deg,#f3e4c8,#f5d7dc 50%,#a9d7ee)" role="img" aria-label="Photo of children painting and crafting"></div>
<div class="abs gallery-tile" style="left:776px;top:2693px;background:radial-gradient(ellipse 50px 110px at 30px 110px,rgba(50,70,110,.85),rgba(50,70,110,0) 100%),radial-gradient(ellipse 70px 60px at 280px 160px,rgba(140,90,60,.8),rgba(140,90,60,0) 100%),radial-gradient(ellipse 90px 70px at 150px 150px,rgba(240,200,215,.95),rgba(240,200,215,0) 100%),linear-gradient(120deg,#6c7f98,#e9d8dc 55%,#f4eef0)" role="img" aria-label="Photo of a girl reading a book"></div>
<div class="abs gallery-tile" style="left:111px;top:2931px;background:radial-gradient(ellipse 100px 60px at 120px 150px,rgba(240,180,40,.95),rgba(240,180,40,0) 100%),radial-gradient(ellipse 70px 70px at 90px 80px,rgba(140,80,45,.85),rgba(140,80,45,0) 100%),linear-gradient(120deg,#efe9e2,#d8cbbd 50%,#b68a60)" role="img" aria-label="Photo of two kids laughing on a sofa"></div>
<div class="abs gallery-tile" style="left:443px;top:2931px;background:radial-gradient(ellipse 120px 40px at 160px 190px,rgba(110,170,80,.9),rgba(110,170,80,0) 100%),radial-gradient(ellipse 60px 60px at 90px 110px,rgba(230,70,110,.75),rgba(230,70,110,0) 100%),radial-gradient(ellipse 150px 60px at 160px 30px,rgba(80,120,60,.8),rgba(80,120,60,0) 100%),linear-gradient(180deg,#6f9a4f,#d8d6c6 50%,#7fb25a)" role="img" aria-label="Photo of kids doing yoga outdoors in a park"></div>
<div class="abs gallery-tile" style="left:776px;top:2931px;background:radial-gradient(ellipse 60px 80px at 60px 130px,rgba(60,60,70,.85),rgba(60,60,70,0) 100%),radial-gradient(ellipse 60px 80px at 250px 140px,rgba(130,130,120,.8),rgba(130,130,120,0) 100%),radial-gradient(ellipse 70px 80px at 160px 120px,rgba(235,215,200,.9),rgba(235,215,200,0) 100%),linear-gradient(120deg,#5a4a36,#a88c70 50%,#6f7c4e)" role="img" aria-label="Photo of happy children playing outside"></div>

<!-- footer -->
<footer class="abs footer"></footer>
<div class="abs title-row" style="top:3310px"><span class="brand-name" style="font-size:22px">SunnyPawTots</span></div>
<div class="abs foot-nav">
  <span>YOGA</span><span>|</span><span>STORIES</span><span>|</span><span>MUSIC</span><span>|</span><span>SECRET SONG</span><span>|</span><span>CRAFTING</span><span>|</span><span>OUR CONCEPT</span><span>|</span><span>CONTACT</span>
</div>
<div class="abs foot-contact">
  <svg width="14" height="14" viewBox="0 0 24 24"><path fill="#d6498a" d="M6.6 10.8a15.1 15.1 0 0 0 6.6 6.6l2.2-2.2a1 1 0 0 1 1-.25 11.4 11.4 0 0 0 3.6.57 1 1 0 0 1 1 1V20a1 1 0 0 1-1 1A17 17 0 0 1 3 4a1 1 0 0 1 1-1h3.5a1 1 0 0 1 1 1c0 1.25.2 2.45.57 3.57a1 1 0 0 1-.25 1z"/></svg>
  <span>+61 (0) 3 9000 1234</span><span style="margin:0 6px">|</span>
  <svg width="16" height="12" viewBox="0 0 16 12"><rect width="16" height="12" rx="1.5" fill="#d6498a"/><path d="M1 1.5l7 5 7-5" fill="none" stroke="#1e1e1e" stroke-width="1.4"/></svg>
  <span>info@sunnypawtots.com</span>
</div>
<span class="abs social first" style="left:518px" aria-label="Social link"></span>
<span class="abs social" style="left:561px" aria-label="Social link"></span>
<span class="abs social" style="left:603px" aria-label="Social link"></span>
<span class="abs social" style="left:646px" aria-label="Social link"></span>
<div class="abs foot-rule"></div>
<p class="abs copyright">© 2022 <b>SUNNY PAW TOTS</b> / All Rights Reserved</p>

</body>
</html>
```